High Quality fast food restaurant - Tomanyo

Tomanyo is a fast food company with its target's focused on logistic, simplicity, high quality, freshness and modern.

We need a web design where the customers can get a complete idea of our high quality completeness, we want to take fast food to a new upper level.

We would like to see the colours of wood and metal. Pictures have been attached of our local.

We would like to have something in similar to: http://www.qpz.example/
Updates

Images for the food we are going to sell can be found here: http://shrt.example/uWQa7

It will be the images with rice, french fries or pita bread.

Target Market(s)

The fast food eating people between sloppy food and restaurant level.

Industry/Entity Type

Fast Food Restaurant

Requirements
Should not have
• No Flash or Java

```html
<!DOCTYPE html>
<html lang="en">
<head>
<meta charset="utf-8">
<title>Tomanyo – Location</title>
<link href="https://fonts.googleapis.com/css2?family=Alfa+Slab+One&family=Marcellus+SC&family=Arimo:wght@400;700&display=swap" rel="stylesheet">
<style>
  :root {
    --wood-dark: #2a140b;
    --wood-mid: #4a2516;
    --wood-light: #5a2e1c;
    --teal: #1a7f73;
    --cream: #fdf1d0;
    --cream-deep: #f3dfae;
    --ink: #111111;
    --brown-text: #3a2212;
    --white: #ffffff;
  }
  * { margin: 0; padding: 0; box-sizing: border-box; }
  html, body { width: 1200px; height: 1000px; overflow: hidden; background: var(--white); }
  body { position: relative; font-family: "Arimo", Arial, sans-serif; color: var(--ink); }

  .site-header {
    position: absolute; left: 0; top: 0; width: 1200px; height: 118px;
    background: linear-gradient(180deg, var(--wood-dark) 0%, var(--wood-mid) 50%, var(--wood-dark) 100%);
  }
  .brand {
    position: absolute; left: 158px; top: 36px;
    font-family: "Alfa Slab One", Georgia, serif; font-size: 33px; color: var(--white);
    letter-spacing: 1px;
  }
  .main-nav a {
    position: absolute; top: 94px; font-family: "Marcellus SC", Georgia, serif;
    font-size: 13px; letter-spacing: 1.6px; color: var(--white); text-decoration: none;
  }
  .main-nav .is-active {
    top: 0; left: 792px; width: 100px; height: 125px; background: var(--teal);
    padding-top: 94px; text-align: center;
  }

  .hero {
    position: absolute; left: 0; top: 118px; width: 1200px; height: 531px;
    background: radial-gradient(ellipse at 25% 40%, #f2d9a4 0%, var(--cream) 55%, var(--cream-deep) 100%);
  }
  .hero-title {
    position: absolute; left: 153px; top: 108px; font-size: 20px; font-weight: 400;
    color: var(--brown-text);
  }
  .hero-info {
    position: absolute; left: 153px; top: 173px; font-size: 14px; line-height: 25px;
    color: var(--brown-text);
  }
  .hero-info .hours { margin-top: 25px; }
  .map {
    position: absolute; left: 526px; top: 29px; width: 477px; height: 480px;
    background: linear-gradient(135deg, #ece8dc 0%, #e5e1cf 50%, #cfe2b5 75%, #a9c8e6 100%);
  }

  .dish-band {
    position: absolute; left: 0; top: 649px; width: 1200px; height: 159px;
    background: linear-gradient(180deg, var(--wood-dark) 0%, var(--wood-light) 50%, var(--wood-dark) 100%);
  }
  .dish {
    position: absolute; top: 675px; width: 176px; height: 176px; border-radius: 50%;
    background: radial-gradient(circle at 50% 55%, #e8d3b0 0%, #b8703e 55%, #5b2a16 100%);
  }
  .price {
    position: absolute; top: 693px; width: 48px; height: 48px; border-radius: 50%;
    background: var(--teal); color: var(--white); font-family: Georgia, serif; font-size: 11px;
    display: flex; align-items: center; justify-content: center;
  }

  .menu-intro { position: absolute; left: 174px; top: 871px; width: 870px; }
  .menu-intro h2 { font-size: 16px; font-weight: 400; }
  .menu-intro p { margin-top: 2px; font-size: 13px; line-height: 16px; text-align: center; }

  .footer-nav a {
    position: absolute; top: 985px; font-size: 10px; font-weight: 700; color: var(--ink);
    text-decoration: none; text-transform: uppercase;
  }
  .social { position: absolute; right: 170px; top: 982px; font-size: 12px; font-weight: 700; }
  .social span { margin-left: 10px; }
</style>
</head>
<body>
  <header class="site-header">
    <div class="brand">TOMANYO</div>
    <nav class="main-nav">
      <a href="#" style="left:526px">HOME</a>
      <a href="#" style="left:599px">MENU</a>
      <a href="#" style="left:674px">FRESH OFFERS</a>
      <a href="#" class="is-active">LOCATION</a>
      <a href="#" style="left:909px">CONTACT US</a>
    </nav>
  </header>

  <section class="hero" role="img" aria-label="Soft background photo of a bowl of broccoli cheese soup and pita bread">
    <h1 class="hero-title">Our Location &amp; Timing :</h1>
    <div class="hero-info">
      <p>Lorem ipsum dolor sit amet, consectetuer<br>adipiscing elit, sed diam nonummy nibh<br>euismod tincidunt ut laor<br>eet dolore &nbsp;VA - 40938127<br>magna aliquam erat volutpat</p>
      <p class="hours">Weekdays - 8.00 a.m - 11.00 p.m<br>Weekends - 7.30 a.m - 11.30 p.m</p>
    </div>
    <div class="map" role="img" aria-label="Street map showing the restaurant location with a pin"></div>
  </section>

  <section class="dish-band" role="img" aria-label="Dark wood texture band"></section>
  <div class="dish" style="left:153px" role="img" aria-label="Wrap with french fries and juice"></div>
  <div class="dish" style="left:392px" role="img" aria-label="Stuffed pita bread on a plate"></div>
  <div class="dish" style="left:631px" role="img" aria-label="Falafel wrap with tomato and sauce"></div>
  <div class="dish" style="left:878px" role="img" aria-label="Grilled chicken pita wraps"></div>
  <div class="price" style="left:136px">$ 32.99</div>
  <div class="price" style="left:377px">$ 22.99</div>
  <div class="price" style="left:614px">$ 40.99</div>
  <div class="price" style="left:860px">$ 20.99</div>

  <section class="menu-intro">
    <h2>MENU</h2>
    <p>Lorem ipsum dolor sit amet, consectetur adipisicing elit, sed do eiusmod tempor incididunt ut labore et dolore magna aliqua. Ut enim ad minim veniam, quis nostrud exercitation ullamco laboris nisi ut aliquip ex ea commodo consequat.Duis aute irure dolor in reprehenderit in voluptate velit esse cillum dolore eu fugiat nulla pariatur. Excepteur sint occaecat cupidatat non proident</p>
  </section>

  <footer>
    <nav class="footer-nav">
      <a href="#" style="left:174px">Home</a>
      <a href="#" style="left:228px">Menu</a>
      <a href="#" style="left:283px">Fresh Offers</a>
      <a href="#" style="left:381px">Location</a>
      <a href="#" style="left:455px">Contact Us</a>
    </nav>
    <div class="social"><span>Faceplace</span><span>Chirper</span><span>Circleup</span></div>
  </footer>
</body>
</html>
```